Tidewell Recovery Business Card Design

Professional and clean design. The design colors should flow with the logo. Two-sided card with the website on the back which is:

www.TidewellRecovery.example.

"Specializing in Water Damage Restoration"

On the front I need the name, email, phone, and logo.

Name: Dorian Vashti
Email: Dorian@TidewellRecovery.example
Phone: 555-318-2046 for now

I only have the Preview and Thumbnail right now but should have the source files uploaded within a day or two.

Target Market(s)

Flood victims, home owners with water damage from busted pipes etc...

Industry/Entity Type

Business

Contact Information for Business Card

Name: Dorian Vashti

Font styles to use
Serif
Sans Serif

```html
<!DOCTYPE html>
<html lang="en">
<head>
<meta charset="UTF-8">
<title>Tidewell Recovery Business Card</title>
<link rel="stylesheet" href="https://fonts.googleapis.com/css2?family=Cinzel:wght@600&family=Roboto:wght@400;500&display=swap">
<style>
  :root {
    --brand-blue: #3a9fdc;
    --brand-blue-deep: #2f8fcf;
    --card-white: #ffffff;
    --stage: #e9ecef;
    --shadow: rgba(20, 40, 60, 0.22);
  }
  * { box-sizing: border-box; margin: 0; padding: 0; }
  html, body {
    width: 1200px; height: 950px; overflow: hidden;
    background: var(--stage);
    font-family: "Roboto", Arial, sans-serif;
  }
  .stage {
    width: 1200px; height: 950px;
    display: flex; flex-direction: column;
    align-items: center; justify-content: center; gap: 34px;
  }
  .card {
    position: relative;
    width: 760px; height: 434px;
    border-radius: 4px; overflow: hidden;
    box-shadow: 0 10px 26px var(--shadow);
  }

  /* Back side */
  .card-back {
    background: var(--brand-blue);
    color: var(--card-white);
    display: flex; flex-direction: column;
    align-items: center; justify-content: center;
  }
  .back-mark {
    width: 150px; height: 150px; border-radius: 50%;
    background: var(--card-white);
  }
  .back-name {
    margin-top: 22px;
    font-family: "Cinzel", Georgia, serif; font-weight: 600;
    font-size: 30px; letter-spacing: 2px;
  }
  .back-tagline {
    margin-top: 34px; font-size: 17px; letter-spacing: 0.4px;
  }
  .back-web {
    margin-top: 8px; font-size: 14px; opacity: 0.95;
  }

  /* Front side */
  .card-front { background: var(--card-white); }
  .front-roof {
    position: absolute; inset: 0;
    background: var(--brand-blue);
    clip-path: polygon(57% 0, 100% 36%, 100% 100%, 31% 100%);
  }
  .front-brand {
    position: absolute; left: 48px; top: 150px;
    display: flex; align-items: center; gap: 14px;
  }
  .brand-dot {
    width: 62px; height: 62px; border-radius: 50%;
    background: var(--brand-blue);
    flex: none;
  }
  .brand-name {
    font-family: "Cinzel", Georgia, serif; font-weight: 600;
    font-size: 27px; line-height: 1.15; color: var(--brand-blue);
    letter-spacing: 1px;
  }
  .front-contact {
    position: absolute; left: 460px; top: 118px;
    color: var(--card-white);
  }
  .contact-dot {
    width: 42px; height: 42px; border-radius: 50%;
    background: var(--card-white);
    margin: 0 0 22px 52px;
  }
  .contact-name {
    font-size: 22px; font-weight: 500; margin-bottom: 16px;
  }
  .contact-list { list-style: none; font-size: 15px; }
  .contact-list li {
    display: flex; align-items: center; gap: 8px; margin-bottom: 8px;
  }
  .contact-list svg { width: 15px; height: 15px; flex: none; }
</style>
</head>
<body>
<main class="stage">
  <section class="card card-back" aria-label="Card back">
    <div class="back-mark"></div>
    <div class="back-name">TIDEWELL RECOVERY</div>
    <p class="back-tagline">Specializing In Water Damage Restoration</p>
    <p class="back-web">www.TidewellRecovery.example</p>
  </section>

  <section class="card card-front" aria-label="Card front">
    <div class="front-roof"></div>
    <div class="front-brand">
      <div class="brand-dot"></div>
      <div class="brand-name">TIDEWELL<br>RECOVERY</div>
    </div>
    <div class="front-contact">
      <div class="contact-dot"></div>
      <h1 class="contact-name">Dorian Vashti</h1>
      <ul class="contact-list">
        <li>
          <svg viewBox="0 0 16 16" aria-hidden="true"><path fill="#fff" d="M3.5 1.5l2.5 0 1 3.2-1.6 1.2a8 8 0 0 0 4.7 4.7l1.2-1.6 3.2 1v2.5c0 .8-.7 1.5-1.5 1.5A12.5 12.5 0 0 1 2 3c0-.8.7-1.5 1.5-1.5z"/></svg>
          555-318-2046 for now
        </li>
        <li>
          <svg viewBox="0 0 16 16" aria-hidden="true"><rect x="1" y="3" width="14" height="10" rx="1" fill="#fff"/><path d="M1.5 3.8L8 9l6.5-5.2" fill="none" stroke="#3a9fdc" stroke-width="1.3"/></svg>
          Dorian@TidewellRecovery.example
        </li>
        <li>
          <svg viewBox="0 0 16 16" aria-hidden="true"><circle cx="8" cy="8" r="6.5" fill="none" stroke="#fff" stroke-width="1.6"/><path d="M1.5 8h13M8 1.5c-3 3.5-3 9.5 0 13M8 1.5c3 3.5 3 9.5 0 13" fill="none" stroke="#fff" stroke-width="1.2"/></svg>
          www.TidewellRecovery.example
        </li>
      </ul>
    </div>
  </section>
</main>
</body>
</html>
```